Employee Wellbeing Model Graphic Design

A visual/graphic representation of our Employee Wellbeing model.
Our model is a combination of the Ara Kōrero Ahi model of health and wellbeing and the wellbeing continuum.
We would like the visual to be on one page. The design should be modern and simple.
The powerpoint attached shows the information we are wanting to share with our employees about our wellbeing programme.

Target Market(s)

Our employees

Industry/Entity Type

Event Management

Font styles to use
Sans Serif
Other font styles liked:
• calibri light

Colors
00AB8E
00BBA5
67D7C9
C6EFE9
E9F9F6

```html
<!DOCTYPE html>
<html lang="en">
<head>
<meta charset="utf-8">
<title>Our Wellbeing Framework</title>
<link href="https://fonts.googleapis.com/css2?family=Open+Sans:ital,wght@0,400;0,600;0,700;1,400&display=swap" rel="stylesheet">
<style>
:root{
  --teal:#0DB8A5;
  --teal-dark:#00AB8E;
  --teal-faint:#E5F3F1;
  --ink:#1d1d1d;
  --heading:#4a4a4a;
  --unwell:#E8206A;
  --struggling:#F5A04A;
  --ok:#D2C42A;
  --thriving:#5DBB6A;
}
*{margin:0;padding:0;box-sizing:border-box}
html,body{width:893px;height:1200px;overflow:hidden;background:#fff}
body{font-family:"Open Sans",Arial,sans-serif;color:var(--ink)}
.page{position:relative;width:893px;height:1200px;overflow:hidden;background:#fff}
.abs{position:absolute}

.header-band{left:0;top:0;width:633px;height:84px;background:var(--teal);clip-path:polygon(0 0,100% 0,94.3% 100%,0 100%)}
.page-title{left:62px;top:24px;color:#fff;font-weight:700;font-size:30px;letter-spacing:.3px}
.brand{left:640px;top:30px;width:230px;text-align:center;color:var(--teal-dark);font-weight:700;font-size:22px;line-height:28px}

.model-figure{left:21px;top:147px;width:275px;height:171px;background:var(--teal);border-radius:4px}
.model-heading{left:309px;top:128px;font-size:23px;font-weight:700;color:var(--heading)}
.model-intro{left:309px;top:162px;width:530px;font-size:12.4px;line-height:17px}

.pill{height:19px;width:174px;background:var(--teal);color:#fff;font-weight:600;font-size:11px;line-height:19px;padding-left:10px;border-radius:3px}
.pill-note{font-size:11px;font-style:italic;color:#333}

.scale-label{font-size:11px;font-weight:700;text-align:center;width:120px}
.unwell{color:var(--unwell)}.struggling{color:var(--struggling)}.ok{color:var(--ok)}.thriving{color:var(--thriving)}
.scale-bar{left:110px;width:750px;height:12px;border-radius:6px;background:linear-gradient(90deg,var(--unwell),var(--struggling) 33%,var(--ok) 66%,var(--thriving))}

.side-tab{left:0;width:82px;background:var(--teal);border-radius:0 22px 22px 0}
.side-tab .tab-text{position:absolute;left:50%;top:50%;transform:translate(-50%,-50%) rotate(-90deg);white-space:nowrap;color:#fff;text-align:center;font-size:14px;font-weight:700;line-height:18px}
.tab-text em{font-weight:400;display:block}

.lead{left:112px;width:752px;font-size:11.2px;font-style:italic;line-height:15.5px}
.list{list-style:none;font-size:11.3px;line-height:15.6px}
.list li{position:relative;padding-left:11px}
.list li::before{content:"•";position:absolute;left:0}

.approach-head{font-size:11.5px;font-weight:700;color:var(--teal)}
.approach-sub{font-size:11.5px}
.programme-title{left:0;width:968px;text-align:center;top:796px;font-size:15.5px;font-weight:700;color:var(--teal)}

.faint-house{left:0;top:932px;width:425px;height:268px;background:var(--teal-faint)}
</style>
</head>
<body>
<main class="page">
  <div class="abs header-band"></div>
  <h1 class="abs page-title">OUR WELLBEING FRAMEWORK</h1>
  <div class="abs brand">Pūkeko Events</div>

  <div class="abs model-figure" role="img" aria-label="Illustration of a meeting house representing the four walls of the Ara Kōrero Ahi model"></div>
  <h2 class="abs model-heading">ARA KŌRERO AHI</h2>
  <p class="abs model-intro">When all these things are in balance, we thrive. When one or more of these is out of balance our wellbeing is impacted. By aligning workplace activities with Ara Kōrero Ahi, organizations can create an environment where well-being is valued, and employees thrive</p>

  <div class="abs pill" style="left:312px;top:250px">TAHA HINESARE</div>
  <div class="abs pill-note" style="left:312px;top:273px">• Mental/Emotional Heath</div>
  <div class="abs pill" style="left:492px;top:250px">TAHA WHANAU</div>
  <div class="abs pill-note" style="left:492px;top:273px">• Family/Community Health</div>
  <div class="abs pill" style="left:675px;top:250px">WHENUA</div>
  <div class="abs pill-note" style="left:675px;top:273px">• Land/Roots</div>
  <div class="abs pill" style="left:312px;top:293px">TANA TINANA</div>
  <div class="abs pill-note" style="left:312px;top:317px">• Physical Health</div>
  <div class="abs pill" style="left:492px;top:293px">TAHA WAIRUA</div>
  <div class="abs pill-note" style="left:492px;top:317px">• Spiritual Health</div>

  <div class="abs scale-label unwell" style="left:140px;top:369px">UNWELL</div>
  <div class="abs scale-label struggling" style="left:332px;top:369px">STRUGGLING</div>
  <div class="abs scale-label ok" style="left:527px;top:369px">GOING OK</div>
  <div class="abs scale-label thriving" style="left:721px;top:369px">THRIVING</div>
  <div class="abs scale-bar" style="top:390px"></div>

  <div class="abs side-tab" style="top:389px;height:251px"><div class="tab-text">The Wellbeing Continuum</div></div>

  <p class="abs lead" style="top:408px">People can have a range of mental health experiences across the continuum that will change over time. It is usual to cycle across the Thriving and Going Ok parts of the spectrum.</p>

  <ul class="abs list" style="left:112px;top:446px;width:170px">
    <li>People who are mentally unwell and/or have a diagnosed mental illness</li>
    <li>Severe and persistent functional impairment</li>
    <li>Neurochemical process outside of the individuals’ control is often established</li>
  </ul>
  <ul class="abs list" style="left:300px;top:446px;width:185px">
    <li>People who don’t meet the criteria for a diagnosable mental illness, but who may be highly stressed or distressed</li>
    <li>More severe and persistent functional impairment</li>
    <li>A mental health problem develops</li>
    <li>Usual coping mechanisms may not suffice or don’t have the same impact</li>
  </ul>
  <ul class="abs list" style="left:492px;top:446px;width:205px">
    <li>People who lack general mental wellbeing and a sense of being reasonably happy with life</li>
    <li>Often show as disengaged and unmotivated, lack meaning and purpose in their daily lives</li>
    <li>Likely to have higher rates of physical illness and workplace accidents</li>
    <li>People develop coping mechanisms which can be applied to help revert to full mental health – thriving</li>
  </ul>
  <ul class="abs list" style="left:701px;top:446px;width:165px">
    <li>People who are mentally unwell and/or have a diagnosed mental illness</li>
    <li>Severe and persistent functional impairment</li>
    <li>Neurochemical process outside of the individuals’ control is often established</li>
  </ul>

  <div class="faint-house abs" role="img" aria-label="Faint meeting house illustration in the background"></div>

  <div class="abs scale-label unwell" style="left:140px;top:668px">UNWELL</div>
  <div class="abs scale-label struggling" style="left:332px;top:668px">STRUGGLING</div>
  <div class="abs scale-label ok" style="left:527px;top:668px">GOING OK</div>
  <div class="abs scale-label thriving" style="left:721px;top:668px">THRIVING</div>
  <div class="abs scale-bar" style="top:689px"></div>

  <div class="abs side-tab" style="top:689px;height:299px"><div class="tab-text">Applying the Wellbeing Continuum<em>Our Wellbeing Initiatives</em></div></div>

  <p class="abs lead" style="top:707px">Our approach is to provide a programme of wellbeing interventions across the continuum, and ensure our initiatives align with the Ara Kōrero Ahi model by providing support for physical health, mental/emotional health, family and community health, spiritual health and connection to whenua.</p>

  <div class="abs" style="left:112px;top:758px"><div class="approach-head">Treatment</div><div class="approach-sub">Providing Help, Supporting Recovery</div></div>
  <div class="abs" style="left:354px;top:758px"><div class="approach-head">Building Capability</div><div class="approach-sub">Changing Mindsets, Raising Awareness</div></div>
  <div class="abs" style="left:620px;top:758px"><div class="approach-head">Prevention</div><div class="approach-sub">Reducing Risks, Staying Well</div></div>

  <h3 class="abs programme-title">OUR PROGRAMME OF WELLBEING INITIATIVES</h3>

  <ul class="abs list" style="left:112px;top:822px;width:235px">
    <li>Occupational Counselling (OCP)</li>
    <li>Domestic Violence Leave</li>
    <li>Injury Management (Tiaki Health)</li>
    <li>Psychological First Aiders</li>
  </ul>
  <ul class="abs list" style="left:354px;top:822px;width:260px">
    <li>Wellbeing Intranet Site</li>
    <li>Wellbeing Training Module in LearnPath</li>
    <li>Lend a Hand (volunteer) Day</li>
    <li>Positive Leadership Programme</li>
    <li>Regular Staff Engagement Activities</li>
    <li>Wellbeing Campaigns</li>
    <li>Culture Committee</li>
    <li>Clear Path e-learning for Managers</li>
  </ul>
  <ul class="abs list" style="left:620px;top:822px;width:232px">
    <li>Wellness Days</li>
    <li>Annual Health Monitoring</li>
    <li>Flu Vaccinations</li>
    <li>Bullying &amp; Harassment Prevention Policy</li>
    <li>Flexible Work Options</li>
    <li>Fatigue Management Guidelines</li>
    <li>Recreation Leave Purchase</li>
    <li>Health and Wellbeing Policy</li>
    <li>Sick leave available from day 1 of employment</li>
    <li>RideLink for Business</li>
  </ul>
</main>
</body>
</html>
```